Bref créative
Business Cards/Letterhead for a Private Equity Real Estate Company
KTR Commercial
Simple
H. Dalton Greave
President
4780 Brambling Road
Suite 610
Atlanta, GA 30342
dalton@ktrcommercial.net
http://ktrcommercial.net/
We think we want the logo on one side and then all the written information on the other. Open to seeing different suggestions, though. Thanks for everyone who participates!

```html
<!DOCTYPE html>
<html lang="en">
<head>
<meta charset="utf-8">
<title>KTR Commercial — Stationery Set</title>
<link rel="stylesheet" href="https://fonts.googleapis.com/css2?family=Open+Sans:wght@400;600;700&display=swap">
<style>
  :root {
    --backdrop: #ffffff;
    --paper: #ffffff;
    --paper-edge: #e4e4e4;
    --ink: #4a4a4a;
    --ink-soft: #8a8a8a;
    --ink-faint: #b5b5b5;
    --mark: #5a5a5a;
    --accent: #b8292f;
  }
  * { box-sizing: border-box; margin: 0; padding: 0; }
  html, body { width: 1200px; height: 936px; overflow: hidden; background: var(--backdrop); }
  body { font-family: "Open Sans", Arial, sans-serif; color: var(--ink); position: relative; }

  .sheet {
    position: absolute;
    background: var(--paper);
    border: 1px solid var(--paper-edge);
    box-shadow: 0 2px 8px rgba(0,0,0,0.12);
  }

  /* Brand name block */
  .brand { display: flex; align-items: center; gap: 6px; }
  .brand-square { background: var(--mark); flex: none; }
  .brand-name {
    font-family: "Open Sans", Arial, sans-serif;
    font-weight: 700;
    color: var(--mark);
    text-transform: uppercase;
    letter-spacing: 0.06em;
    line-height: 1;
    white-space: nowrap;
  }

  /* Letterhead */
  .letterhead { left: 254px; top: 13px; width: 335px; height: 601px; }
  .letterhead .brand { position: absolute; left: 0; right: 0; top: 24px; justify-content: center; }
  .letterhead .brand-square { width: 12px; height: 12px; }
  .letterhead .brand-name { font-size: 13px; }
  .letter-body { position: absolute; left: 38px; right: 38px; top: 88px; font-size: 5.2px; line-height: 1.7; color: var(--ink-soft); }
  .letter-body p { margin-bottom: 9px; }
  .letter-body .salutation { color: var(--ink); font-weight: 600; margin-bottom: 0; }
  .signature-mark { width: 44px; height: 14px; background: linear-gradient(90deg, #d8d8d8, #efefef); margin: 2px 0 6px; }
  .signer { color: var(--ink); font-weight: 600; margin-bottom: 0 !important; }
  .letter-footer { position: absolute; left: 0; right: 0; bottom: 22px; text-align: center; font-size: 5.2px; line-height: 1.8; color: var(--ink-soft); }
  .letter-footer .sep { color: var(--accent); padding: 0 3px; }

  /* Presentation folder */
  .folder { left: 617px; top: 13px; width: 461px; height: 601px; }
  .folder .brand { position: absolute; left: 0; right: 0; top: 268px; justify-content: center; gap: 12px; }
  .folder .brand-square { width: 34px; height: 34px; }
  .folder .brand-name { font-size: 34px; }
  .folder-url { position: absolute; right: 34px; bottom: 26px; font-size: 9px; letter-spacing: 0.32em; color: var(--ink-soft); }

  /* Business cards */
  .card { width: 184px; height: 100px; }
  .card-front { left: 71px; top: 655px; }
  .card-info { left: 270px; top: 655px; }
  .card-blank { left: 71px; top: 773px; }
  .card .brand { position: absolute; left: 12px; top: 12px; gap: 4px; }
  .card .brand-square { width: 8px; height: 8px; }
  .card .brand-name { font-size: 8.5px; }
  .card-person { position: absolute; left: 12px; top: 40px; font-size: 5px; line-height: 1.5; }
  .card-person .name { color: var(--accent); font-weight: 700; font-size: 5.6px; }
  .card-person .role { color: var(--ink-soft); }
  .card-contact { position: absolute; left: 12px; top: 40px; font-size: 4.6px; line-height: 1.65; color: var(--ink-soft); }
  .card-contact .web { color: var(--accent); }

  /* Envelope */
  .envelope { left: 477px; top: 655px; width: 614px; height: 215px; }
  .envelope-flap { position: absolute; inset: 0; }
  .envelope-url { position: absolute; right: 60px; top: 22px; font-size: 9px; letter-spacing: 0.3em; color: var(--ink-soft); }
</style>
</head>
<body>

  <!-- Letterhead -->
  <section class="sheet letterhead" aria-label="Letterhead">
    <div class="brand"><span class="brand-square"></span><span class="brand-name">KTR Commercial</span></div>
    <div class="letter-body">
      <p>July 4, 2024</p>
      <p class="salutation">Dear Partner,</p>
      <p>Investor Relations, Atlanta, Georgia</p>
      <p>We are pleased to confirm our review of the commercial portfolio discussed at our recent meeting. Our team has completed site visits, tenant interviews and a detailed market comparison for each of the properties under consideration this quarter.</p>
      <p>The enclosed summary outlines projected returns, financing options and the management plan we recommend. Please share it with your partners and let us know a convenient time next week to walk through the figures together.</p>
      <p>Thank you again for your trust in our firm. We look forward to building a lasting partnership.</p>
      <p>Best Regards,</p>
      <div class="signature-mark" role="img" aria-label="Handwritten signature"></div>
      <p class="signer">H. Dalton Greave</p>
      <p>President, KTR Commercial</p>
    </div>
    <div class="letter-footer">
      <div>4780 Brambling Road, Suite 610<span class="sep">|</span>Atlanta, GA 30342<span class="sep">|</span>www.ktrcommercial.net</div>
      <div>(404) 555-0142<span class="sep">|</span>(404) 555-0187<span class="sep">|</span>dalton@ktrcommercial.net</div>
    </div>
  </section>

  <!-- Presentation folder -->
  <section class="sheet folder" aria-label="Presentation folder">
    <div class="brand"><span class="brand-square"></span><span class="brand-name">KTR Commercial</span></div>
    <div class="folder-url">www.ktrcommercial.net</div>
  </section>

  <!-- Business card, name side -->
  <section class="sheet card card-front" aria-label="Business card front">
    <div class="brand"><span class="brand-square"></span><span class="brand-name">KTR Commercial</span></div>
    <div class="card-person">
      <div class="name">H. Dalton Greave</div>
      <div class="role">President</div>
      <div class="role">dalton@ktrcommercial.net</div>
    </div>
  </section>

  <!-- Business card, contact side -->
  <section class="sheet card card-info" aria-label="Business card contact side">
    <div class="brand"><span class="brand-square"></span><span class="brand-name">KTR Commercial</span></div>
    <div class="card-contact">
      <div>4780 Brambling Road, Suite 610</div>
      <div>Atlanta, GA 30342</div>
      <div>(404) 555-0142</div>
      <div class="web">http://ktrcommercial.net/</div>
    </div>
  </section>

  <!-- Business card, plain reverse -->
  <section class="sheet card card-blank" aria-label="Business card reverse"></section>

  <!-- Envelope -->
  <section class="sheet envelope" aria-label="Envelope">
    <svg class="envelope-flap" width="614" height="215" viewBox="0 0 614 215" aria-hidden="true">
      <polyline points="0,0 307,96 614,0" fill="none" stroke="#ececec" stroke-width="1"/>
    </svg>
    <div class="envelope-url">www.ktrcommercial.net</div>
  </section>

</body>
</html>
```